Existing Wix Website Redesign

Our current website is in need of redesign for the wix.com platform. https://www.brackettrails.com.au/ <br/>In addition to the brief below, we need the Website to be Multi – Lingual : English, Japanese, German, Dutch, French, Italian, Chinese Mandarin and Chinese Cantonese & Korean<br/><br/>All the content is already listed on the website. The successful design will implement the website with the current content and edit this including correct headers and URL addresses.<br/><br/>Company Profile-<br/>Orwell’s Treks enhances the travellers' life experience through the wonder, discovery, adventure and cultural immersion of high quality tours throughout Papua New Guinea.<br/><br/>Our mission is to design and conduct safe, educational and exciting tours which:<br/><br/>cater for a range of ages, interests and budgets; respect local communities; promote sustainable tourism, leaving with them special memories.<br/><br/> <br/><br/>The current target demographic for Orwell’s Treks of Papua New Guinea is the 50+ age group, primarily in Australia and New Zealand, but also the United States, Japan, Europe (Germany, France Italy & Britain and also China as it’s outbound visitor market matures and seeks new adventures.<br/><br/>We offer fully escorted small group tours and holidays that are safe, fully organised and guided for all age groups, nationalities and budgets.<br/><br/>PNG is uniquely placed as an attractive destination, showcasing the oldest, authentic surviving culture on earth! <br/><br/>Over 800 tribes generously share their customs, art, music, carvings, costumes and dances at a range of Festivals or “sing sings” held across the highlands and islands of this most picturesque of countries providing visiting culture enthusiasts and photographers with lasting memories and vivid images. Traversing the Pacific’s “Rim of Fire”, visitors are presented with a daily feast of scenery with the best nature has to offer amongst it’s big mountainous jungles and forests, untamed rivers, volcanic landscapes and pristine marine environments. Photograph animals, plants and exotic birds including the globally renowned Birds of Paradise.<br/><br/>The key group to target amongst the over 50’s are the Baby Boomers who are those born between 1946 to 1964.<br/><br/> <br/><br/>Baby boomers are also seeking an authentic experience whilst travelling. They want to go where the locals go, immersing themselves fully to experience and learn about a new culture.<br/><br/>According to the Global Voyage Council, boomers are more likely to seek out educational and cultural experiences. What boomers really want is to be intellectually stimulated, which is why an experienced, knowledgeable and well-trained guide, such as Peter Mallory and those guides that he trains are necessary to attract them to these tours. Peter has immersed himself in the many periods of colonial occupier history along with a sound understanding of the first peoples and their cultures and Melanesian lifestyles.<br/><br/>As a destination Papua New Guinea will attract the baby boomers that are “young at heart” who actively seek out adventure, sometimes as a form of self-discovery. Knowing that they want to experience new adventures while being safe, Orwell’s Treks has created adventure in a semi-controlled environment for the baby boomer.<br/><br/>Orwell’s Treks of Papua New Guinea will be of interest primarily to the “Baby Boomer” demographic in Australia, many who have a fond familiarity with their neighbouring ex-colony. Their parents may have been involved in PNG in the pre-independence era as First and Second World War military personal, “Kiap” patrol officers, nurses, teachers,missionaries, tradesmen or public servants.<br/><br/>Potential visitors will discover a little known destination where the traditional Melanesian culture with over 800 tribes and languages, thrive and where, outside the major regional centres, little has changed in thousands of years.

Target Market(s)

Travel and Tourism

Colors

Designer to choose colors to be used in the design.

Requirements
Must have
• Website to be Multi – Lingual : English, Japanese, German, Dutch, French, Italian, Chinese Mandarin and Chinese Cantonese & Korean
• The successful design will implement the website with the current content and edit this including correct headers and URL addresses.

```html
<!DOCTYPE html>
<html lang="en">
<head>
<meta charset="utf-8">
<title>Orwell’s Treks – Papua New Guinea Tours</title>
<link href="https://fonts.googleapis.com/css2?family=Poppins:wght@500;600;700&family=IBM+Plex+Sans:wght@400;500;600&display=swap" rel="stylesheet">
<style>
:root{
  --green:#b8df95;
  --btn-green:#b5dd92;
  --btn-text:#3d5a22;
  --blue:#6aa3d9;
  --red:#e53f26;
  --orange:#f18526;
  --dark:#262626;
  --nav-dark:#3a3a3a;
  --card:#f5f1f1;
  --ink:#222222;
  --white:#ffffff;
}
*{box-sizing:border-box;margin:0;padding:0}
html,body{width:1200px;height:3287px;overflow:hidden;background:var(--white)}
body{position:relative;font-family:"IBM Plex Sans",Arial,sans-serif;color:var(--ink)}
.abs{position:absolute}
.btn{position:absolute;display:flex;align-items:center;justify-content:center;background:var(--btn-green);color:var(--btn-text);font-family:"IBM Plex Sans",sans-serif;font-weight:600;font-size:12px;text-transform:uppercase}
.btn.white{background:var(--white)}

/* header */
.site-header{position:absolute;top:0;left:0;width:1200px;height:75px;background:var(--white)}
.brand{position:absolute;left:14px;top:22px;display:flex;align-items:center;gap:10px;font-family:"Poppins",sans-serif;font-weight:600;font-size:22px;color:var(--ink)}
.brand-dot{width:22px;height:22px;border-radius:50%;background:var(--ink)}
.lang{position:absolute;left:797px;top:28px;font-weight:600;font-size:14px;display:flex;align-items:center;gap:10px}
.nav-item{position:absolute;top:0;height:75px;display:flex;align-items:center;justify-content:center;font-weight:600;font-size:14px;text-transform:uppercase}
.nav-tours{left:855px;width:118px;background:var(--nav-dark);color:var(--white)}
.nav-gallery{left:973px;width:117px;background:var(--green);color:var(--btn-text)}
.nav-menu{left:1090px;width:110px;background:#000;color:var(--white);gap:8px}

/* hero */
.hero{position:absolute;top:75px;left:0;width:1200px;height:611px;background:linear-gradient(160deg,#6f8fa8 0%,#4d7a58 28%,#2f5a2a 60%,#3f4a2c 100%)}
.hero-title{position:absolute;left:619px;top:160px;font-family:"IBM Plex Sans",sans-serif;font-weight:600;font-size:58px;line-height:60px;color:var(--white);text-transform:uppercase}
.hero .btn{left:626px;top:378px;width:151px;height:55px;font-size:19px}
.hero-dots{position:absolute;left:548px;top:545px;display:flex;gap:14px}
.hero-dots span{width:9px;height:9px;border-radius:50%;background:var(--white)}
.hero-dots span.active{background:#b07a3c}

/* section titles */
.section-title{position:absolute;left:0;width:1200px;text-align:center;font-family:"Poppins",sans-serif;font-weight:700;font-size:30px;color:var(--ink)}
.section-title::after{content:"";display:block;width:46px;height:3px;background:var(--green);margin:10px auto 0}

/* cards */
.card{position:absolute;width:300px;background:var(--card);text-align:center}
.card-media{height:238px}
.card-title{margin-top:25px;font-weight:600;font-size:15px;line-height:19px;text-transform:uppercase}
.card-text{margin:8px auto 0;width:240px;font-size:12px;line-height:17px}
.card-price{margin-top:12px;font-weight:600;font-size:14px}
.card .btn{left:50%;transform:translateX(-50%);width:96px;height:34px}

/* mosaic */
.tile{position:absolute}
.tile-heading{font-family:"Poppins",sans-serif;font-weight:600}
.welcome{left:0;top:1348px;width:499px;height:298px;background:var(--green)}
.welcome .eyebrow{position:absolute;left:131px;top:38px;font-family:"Poppins",sans-serif;font-weight:600;font-size:18px}
.welcome .tile-heading{position:absolute;left:131px;top:60px;font-size:25px}
.welcome p{position:absolute;left:131px;top:110px;width:305px;font-size:14px;line-height:17.5px}
.gallery{left:775px;top:1348px;width:425px;height:298px;background:var(--blue)}
.gallery .tile-heading{position:absolute;left:61px;top:60px;font-size:25px;color:#1f2f45}
.gallery p{position:absolute;left:65px;top:108px;width:275px;font-size:14px;line-height:17.5px;color:#1f2f45}
.birding{left:499px;top:1646px;width:701px;height:260px;background:var(--red);color:var(--white)}
.birding .tile-heading{position:absolute;left:79px;top:56px;font-size:25px}
.birding p{position:absolute;left:81px;top:108px;width:420px;font-size:14px;line-height:17.5px}
.birds{left:222px;top:1906px;width:277px;height:296px;background:var(--orange)}
.birds .tile-heading{position:absolute;left:59px;top:76px;font-size:25px;line-height:28px;color:#2a1a0a}
.goroka{left:499px;top:1906px;width:276px;height:296px;background:var(--dark);color:var(--white)}
.goroka .tile-heading{position:absolute;left:55px;top:76px;font-size:25px;line-height:28px}

/* footer */
.site-footer{position:absolute;left:0;top:2898px;width:1200px;height:389px;background:var(--dark);color:var(--white)}
.site-footer h2{position:absolute;left:131px;top:56px;font-family:"Poppins",sans-serif;font-weight:600;font-size:24px}
.field{position:absolute;left:135px;width:303px;border-bottom:1px solid #bdbdbd;font-size:13px;padding-bottom:8px}
.site-footer .btn{left:133px;top:306px;width:99px;height:39px;font-size:16px}
.info{position:absolute;top:56px;font-size:14px;line-height:17.5px}
.info strong{display:block;font-weight:600;margin-bottom:13px}
.follow{position:absolute;left:600px;top:217px;display:flex;align-items:center;gap:11px;font-weight:600;font-size:14px}
.follow .label{margin-right:13px}
.social{width:30px;height:30px;border-radius:50%}
.copyright{position:absolute;left:600px;top:326px;font-size:14px}
</style>
</head>
<body>

<header class="site-header">
  <div class="brand"><span class="brand-dot"></span>Orwell’s Treks</div>
  <div class="lang">EN
    <svg width="10" height="6" viewBox="0 0 10 6"><path d="M0 0h10L5 6z" fill="#222"/></svg>
  </div>
  <div class="nav-item nav-tours">Tours</div>
  <div class="nav-item nav-gallery">Gallery</div>
  <div class="nav-item nav-menu">Menu
    <svg width="12" height="10" viewBox="0 0 12 10"><path d="M0 1h12M0 5h12M0 9h12" stroke="#fff" stroke-width="2"/></svg>
  </div>
</header>

<section class="hero" role="img" aria-label="Hikers with binoculars on a green hillside overlooking a volcano and bay">
  <h1 class="hero-title">New Britain<br>Sepik River<br>Adventure</h1>
  <div class="btn">Read More</div>
  <div class="hero-dots"><span></span><span></span><span class="active"></span><span></span><span></span></div>
</section>

<h2 class="section-title" style="top:733px">Tours</h2>

<article class="card" style="left:131px;top:825px;height:459px">
  <div class="card-media" role="img" aria-label="Traditional spirit house with costumed figures on a lawn" style="background:linear-gradient(180deg,#8bb3c9,#3f6a2f 55%,#6b8a3a)"></div>
  <h3 class="card-title">Mt Hagen Show –<br>PNG Art &amp; Photo Safari</h3>
  <p class="card-text">Mt Hagen Show - Sepik River Festival - Birds of Paradise Carvings</p>
  <p class="card-price">8,620 USD P.P &nbsp;| &nbsp;12 DAYS</p>
  <div class="btn" style="top:398px">Read More</div>
</article>

<article class="card" style="left:451px;top:825px;height:459px">
  <div class="card-media" role="img" aria-label="White castle behind cherry blossoms under blue sky" style="background:linear-gradient(180deg,#2f8fe0,#8cbde8 45%,#e8c8d6 75%,#c99bb3)"></div>
  <h3 class="card-title">Nippon Under The Cherry<br>Blossoms – Japan</h3>
  <p class="card-text">Tokyo - Kyoto - Osaka - Koyasan - Nara - Kiso Valley - Mt Fuji Kanazawa</p>
  <p class="card-price">7,380 USD P.P | &nbsp;16 DAYS</p>
  <div class="btn" style="top:398px">Read More</div>
</article>

<article class="card" style="left:767px;top:825px;height:459px">
  <div class="card-media" role="img" aria-label="Highland performer in red and yellow ceremonial paint" style="background:linear-gradient(180deg,#cfe3ee,#d98a3a 50%,#b23a1d)"></div>
  <h3 class="card-title">Melanesian Wonderland –<br>Papua New Guinea</h3>
  <p class="card-text">Lake Kutubu Festival - Goroka Show - Agri-tourism - Skull Caves Birds of Paradise</p>
  <p class="card-price">10,560 USD P.P | &nbsp;18 DAYS</p>
  <div class="btn" style="top:398px">Read More</div>
</article>

<section class="tile welcome">
  <p class="eyebrow">Welcome to</p>
  <h2 class="tile-heading">Orwell’s Treks</h2>
  <p>Orwell’s Treks is a tour operator specialising in Papua New Guinea and also Japan. All our destinations offer the ultimate experience for excitement, fun, adventure and cultural interaction.</p>
  <div class="btn white" style="left:134px;top:222px;width:96px;height:34px">Read More</div>
</section>

<div class="tile" role="img" aria-label="Silhouette of a canoe paddler at sunset near stilt houses" style="left:499px;top:1348px;width:276px;height:298px;background:linear-gradient(180deg,#c14a96,#7a2f6a 55%,#2a1530)"></div>

<section class="tile gallery">
  <h2 class="tile-heading">Gallery</h2>
  <p>Papua New Guinea’s birdlife is as diverse as its culture with it’s proliferation of over 800 languages.</p>
  <div class="btn" style="left:68px;top:185px;width:128px;height:33px">View All Images</div>
</section>

<div class="tile" role="img" aria-label="Close-up of a bird of paradise with yellow and green plumage" style="left:0;top:1646px;width:499px;height:556px;background:radial-gradient(circle at 45% 30%,#8fb04a,#5a3a1e 45%,#3c2414 80%)"></div>

<section class="tile birding">
  <h2 class="tile-heading">Birding Expedition in papua new guinea</h2>
  <p>Papua New Guinea’s birdlife is as diverse as its culture with it’s proliferation of over 800 languages.</p>
  <div class="btn" style="left:84px;top:165px;width:95px;height:34px">Read More</div>
</section>

<section class="tile birds">
  <h2 class="tile-heading">Birds of papua<br>new guinea</h2>
  <div class="btn" style="left:63px;top:185px;width:94px;height:34px">Read More</div>
</section>

<section class="tile goroka">
  <h2 class="tile-heading">Goroka show<br>&amp; lake kutubu<br>festival</h2>
  <div class="btn white" style="left:59px;top:185px;width:94px;height:34px">Read More</div>
</section>

<div class="tile" role="img" aria-label="Dancers in feathered headdresses at a village festival" style="left:775px;top:1906px;width:425px;height:296px;background:linear-gradient(180deg,#7aa05a,#8a6a4a 50%,#a5734a)"></div>

<h2 class="section-title" style="top:2263px">Latest Blog</h2>

<article class="card" style="left:131px;top:2371px;height:459px">
  <div class="card-media" role="img" aria-label="Travellers beside an aircraft wreck in the jungle" style="background:linear-gradient(180deg,#9aa39a,#6d7a62 45%,#3d6a2c)"></div>
  <h3 class="card-title">Bougainville - Nature<br>Survived in War Zone</h3>
  <p class="card-text">Bougainville is an ecological wonderland where you can immerse yourself in the splendor of its natural and scenic beauty</p>
  <div class="btn" style="top:400px">Read More</div>
</article>

<article class="card" style="left:451px;top:2371px;height:459px">
  <div class="card-media" role="img" aria-label="Tall thatched spirit house among palm trees" style="background:linear-gradient(180deg,#c9d3c9,#5d7a45 45%,#2e4a22)"></div>
  <h3 class="card-title">The Mighty<br>Sepik River</h3>
  <p class="card-text">We journeyed down the mysterious Sepik River in a motorised dugout canoe, experiencing traditional village life along the way.</p>
  <div class="btn" style="top:400px">Read More</div>
</article>

<article class="card" style="left:767px;top:2371px;height:459px">
  <div class="card-media" role="img" aria-label="Performers in red and yellow costumes at a cultural show" style="background:linear-gradient(180deg,#c43a2a,#e0a42e 50%,#a0281c)"></div>
  <h3 class="card-title">Mt. Hagen Cultural Show:<br>A Feast of Colour</h3>
  <p class="card-text">Following our arrival from Australia, we traversed the stunning PNG Highlands seeking out the beautiful Birds</p>
  <div class="btn" style="top:400px">Read More</div>
</article>

<footer class="site-footer">
  <h2>Contact Us</h2>
  <div class="field" style="top:120px">Name</div>
  <div class="field" style="top:178px">E mail</div>
  <div class="field" style="top:243px">Phone</div>
  <div class="btn">Submit</div>

  <div class="info" style="left:600px"><strong>Address</strong>P.O. Box 4417<br>Ashwood Vale 3192<br>Melbourne</div>
  <div class="info" style="left:773px"><strong>Phone</strong>+61 400 555 017</div>
  <div class="info" style="left:915px"><strong>E mail</strong>info@orwellstreks.com.au</div>

  <div class="follow">
    <span class="label">Follow Us</span>
    <span class="social" style="background:#3b5bb5" aria-label="Social profile"></span>
    <span class="social" style="background:#1d9be6" aria-label="Social profile"></span>
    <span class="social" style="background:#1f2f6e" aria-label="Social profile"></span>
  </div>
  <p class="copyright">Copyright © 2019 All Rights Reserved</p>
</footer>

</body>
</html>
```